Law Firm Website

Our client has never had a website, but their services are similar to: https://www.halbrook-tenney.com.

They are a personal injury attorney, husband, and wife team.

Coding

Coded - Design and coding required

Number of Pages Required

1 page

Font styles to use
Sans Serif

Colors
0054AA
0677BA
7BADD7
CADEEF
E8F1F8

```html
<!DOCTYPE html>
<html lang="en">
<head>
<meta charset="utf-8">
<title>Harborline Law</title>
<link href="https://fonts.googleapis.com/css2?family=Roboto:wght@400;500;700&display=swap" rel="stylesheet">
<style>
:root{
  --blue:#0054AA;
  --blue-mid:#0677BA;
  --blue-soft:#7BADD7;
  --blue-pale:#CADEEF;
  --blue-mist:#E8F1F8;
  --navy:#0A2B7E;
  --navy-deep:#08246B;
  --sky:#1EA7F5;
  --ink:#2A2A2A;
  --text:#666;
  --grey-bg:#F4F4F4;
  --white:#fff;
}
*{margin:0;padding:0;box-sizing:border-box}
html,body{width:1200px;height:3429px;overflow:hidden}
body{position:relative;font-family:'Roboto',Arial,sans-serif;color:var(--ink);background:var(--white)}
.abs{position:absolute}

/* header */
.site-header{left:0;top:0;width:1200px;height:90px;background:linear-gradient(90deg,#0A4FAE,#0B5CC0);color:var(--white)}
.brand{left:112px;top:22px;font-size:28px;font-weight:500;letter-spacing:3px;text-transform:uppercase;color:var(--white)}
.nav{left:407px;top:30px;display:flex;gap:32px;font-size:14px}
.nav a{color:var(--white);text-decoration:none;padding-bottom:6px}
.nav a.active{border-bottom:3px solid var(--white)}
.call-box{left:882px;top:20px;width:40px;height:40px;border:1px solid var(--white)}
.call-label{left:940px;top:20px;font-size:13px}
.call-number{left:940px;top:38px;font-size:21px;font-weight:700}

/* hero */
.hero{left:0;top:90px;width:1200px;height:595px;background:linear-gradient(180deg,#0E1D4E 0%,#1F3F86 45%,#2A4C8E 70%,#1C2F62 100%)}
.hero-title{left:0;top:338px;width:1200px;text-align:center;font-size:54px;font-weight:700;color:var(--white)}
.hero-text{left:250px;top:416px;width:700px;text-align:center;font-size:16.5px;line-height:26px;color:var(--white)}

/* connectors */
.connector{width:2px;background:var(--blue-mid);left:599px}
.connector::before,.connector::after{content:"";position:absolute;left:-2px;width:6px;height:6px;border-radius:50%;background:var(--blue-mid)}
.connector::before{top:-3px}.connector::after{bottom:-3px}

.section-title{left:0;width:1200px;text-align:center;font-size:40px;font-weight:500;color:var(--ink)}
.about-text{left:222px;width:756px;text-align:center;font-size:14.5px;line-height:26px;color:var(--text)}
.btn{display:flex;align-items:center;justify-content:center;background:var(--sky);color:var(--white);font-size:14px;font-weight:700}

/* services */
.services{left:0;top:1200px;width:1200px;height:577px;background:linear-gradient(90deg,#0F58B5,#1776D2 60%,#249FEA)}
.services-title{top:1290px;color:var(--white)}
.card{top:1372px;width:232px;height:302px}
.card-photo{width:232px;height:233px}
.card-label{height:69px;display:flex;align-items:center;justify-content:center;background:var(--navy-deep);color:var(--white);font-size:19px}
.card.selected .card-label{background:var(--white);color:var(--navy)}
.slider-dot{top:1513px;width:36px;height:36px;border-radius:50%;background:var(--navy-deep)}

/* testimonials */
.quote{left:541px;top:1985px;width:444px;font-size:16.5px;line-height:34px;color:#555;text-align:justify}
.quote-name{left:541px;top:2138px;font-size:22px;font-weight:700;color:var(--navy)}
.quote-company{left:541px;top:2174px;font-size:13.5px;color:#777}

/* about me */
.about-me{left:0;top:2347px;width:1200px;height:633px;background:var(--grey-bg)}
.about-me-title{left:111px;top:2438px;font-size:40px;font-weight:500}
.about-me-text{left:111px;width:475px;font-size:14.5px;line-height:26px;color:var(--text);text-align:justify}

/* footer */
.site-footer{left:0;top:2980px;width:1200px;height:449px;background:var(--navy-deep)}
.footer-head{top:3090px;font-size:22px;font-weight:400;color:var(--white)}
.footer-list{top:3138px;list-style:none;font-size:14px;line-height:26px;color:var(--white)}
.footer-list li{display:flex;align-items:flex-start;gap:12px}
.footer-list svg{flex:none;margin-top:9px}
.copyright{left:0;top:3358px;width:1200px;text-align:center;font-size:14px;color:var(--white)}
</style>
</head>
<body>

<header class="site-header abs">
  <div class="brand abs">Harborline Law</div>
  <nav class="nav abs">
    <a class="active" href="#">HOME</a><a href="#">OUR TEAM</a><a href="#">PRACTICE AREAS</a><a href="#">CONTACT US</a>
  </nav>
  <div class="call-box abs">
    <svg width="40" height="40" viewBox="0 0 40 40"><path d="M14 12c1-1 2-1 3 0l2 3c1 1 0 2-1 3 1 2 3 4 5 5 1-1 2-2 3-1l3 2c1 1 1 2 0 3l-2 2c-6 0-15-9-15-15z" fill="#fff"/></svg>
  </div>
  <div class="call-label abs">Call us :</div>
  <div class="call-number abs">+1 555 010 2040</div>
</header>

<section class="hero abs" role="img" aria-label="Night city skyline photograph"></section>
<h1 class="hero-title abs">HARBORLINE LAW FIRM</h1>
<p class="hero-text abs">Lorem ipsum dolor sit amet, consectetur adipiscing elit, sed do eiusmod tempor incididunt ut labore et dolore magna aliqua. Ut enim ad minim veniam, quis nostrud exercitation ullamco laboris nisi ut aliquip ex ea commodo consequat.</p>
<svg class="abs" style="left:592px;top:592px" width="16" height="10" viewBox="0 0 16 10"><path d="M2 2l6 6 6-6" stroke="#fff" stroke-width="2" fill="none"/></svg>
<div class="connector abs" style="top:620px;height:148px"></div>

<h2 class="section-title abs" style="top:780px">ABOUT US</h2>
<p class="about-text abs" style="top:836px">Lorem ipsum dolor sit amet, consectetur adipiscing elit, sed do eiusmod tempor incididunt ut labore et dolore magna aliqua. Ut enim ad minim veniam, quis nostrud exercitation ullamco laboris nisi ut aliquip ex ea commodo consequat. Duis aute irure dolor in reprehenderit in voluptate velit esse cillum dolore eu fugiat nulla pariatur.</p>
<p class="about-text abs" style="top:939px">Excepteur sint occaecat cupidatat nLorem ipsum dolor sit amet, consectetur adipiscing elit, sed do eiusmod tempor incididunt ut labore et dolore magna aliqua. Ut enim ad minim veniam, quis nostrud exercitation ullamco laboris nisi ut aliquip ex ea commodo consequat. Duis aute irure dolor in reprehenderit in voluptate velit esse cillum dolore eu fugiat nulla pariatur. Excepteur sint occaecat cupidatat non proiden</p>
<div class="btn abs" style="left:535px;top:1055px;width:130px;height:42px">VISIT US</div>
<div class="connector abs" style="top:1123px;height:147px;z-index:2"></div>

<section class="services abs" role="img" aria-label="Blue-tinted office desk photograph"></section>
<h2 class="section-title services-title abs">WHAT WE DO</h2>
<div class="slider-dot abs" style="left:38px"><svg width="36" height="36"><path d="M20 12l-6 6 6 6" stroke="#fff" stroke-width="2" fill="none"/></svg></div>
<div class="slider-dot abs" style="left:1126px"><svg width="36" height="36"><path d="M16 12l6 6-6 6" stroke="#fff" stroke-width="2" fill="none"/></svg></div>

<div class="card abs" style="left:112px"><div class="card-photo" role="img" aria-label="Man shaking hands" style="background:linear-gradient(135deg,#c98a6a,#3a5a9a)"></div><div class="card-label">Personal Injury</div></div>
<div class="card selected abs" style="left:360px"><div class="card-photo" role="img" aria-label="Bag of white powder being handed over" style="background:linear-gradient(135deg,#3a3a3a,#8a8a8a 60%,#2b8ad8)"></div><div class="card-label">Dangerous Drugs</div></div>
<div class="card abs" style="left:608px"><div class="card-photo" role="img" aria-label="Damaged truck after accident" style="background:linear-gradient(180deg,#a8c8e8,#5a7a9a 60%,#2a3a4a)"></div><div class="card-label">Car &amp; Truck Accidents</div></div>
<div class="card abs" style="left:856px"><div class="card-photo" role="img" aria-label="Surgeons in an operating room" style="background:linear-gradient(135deg,#d8e4ee,#4a7aa8)"></div><div class="card-label">Medical Malpractice</div></div>

<div class="connector abs" style="top:1700px;height:148px"></div>

<h2 class="section-title abs" style="top:1890px">TESTIMONIALS</h2>
<svg class="abs" style="left:110px;top:2074px" width="30" height="22" viewBox="0 0 30 22"><path d="M28 11H3M12 2L3 11l9 9" stroke="#111" stroke-width="2.5" fill="none"/></svg>
<svg class="abs" style="left:1060px;top:2074px" width="30" height="22" viewBox="0 0 30 22"><path d="M2 11h25M18 2l9 9-9 9" stroke="#111" stroke-width="2.5" fill="none"/></svg>
<svg class="abs" style="left:234px;top:1968px" width="250" height="250" viewBox="0 0 250 250" role="img" aria-label="Client portrait"><circle cx="125" cy="125" r="125" fill="#A6C8E6"/><circle cx="125" cy="125" r="106" fill="#8A9AAE"/></svg>
<p class="quote abs">"John Marlowe is an Excellent Lawyer! One who deeply cares and goes the extra mile for his clients. And his staff are great to speak with. Always friendly and willing to help! Tell 'em Ms J from Ridgeview recommended you!"</p>
<div class="quote-name abs">John Doe</div>
<div class="quote-company abs">Company name</div>

<section class="about-me abs"></section>
<div class="connector abs" style="top:2272px;height:143px"></div>
<h2 class="about-me-title abs">ABOUT ME</h2>
<p class="about-me-text abs" style="top:2503px">Lorem ipsum dolor sit amet, consectetur adipiscing elit, sed do eiusmod tempor incididunt ut labore et dolore magna aliqua. Ut enim ad minim veniam, quis nostrud exercitation ullamco laboris nisi ut aliquip ex ea commodo consequat. Duis aute irure dolor in reprehenderit in voluptate velit esse cillum dolore eu fugiat nulla pariatur.</p>
<p class="about-me-text abs" style="top:2657px">Excepteur sint occaecat cupidatat non proident, sunt in culpa qui officia deserunt mollit anim id est laborum. Lorem ipsum dolor sit amet, consectetur adipiscing elit, sed do eiusmod tempor incididunt ut labore et dolore magna aliqua. Ut enim ad minim veniam, quis nostrud exercitation ullamco laboris nisi ut aliquip ex ea commodo consequat. Duis aute irure dolor in reprehenderit in voluptate velit esse cillum dolore</p>
<div class="btn abs" style="left:111px;top:2835px;width:130px;height:42px">LEARN MORE</div>
<div class="abs" style="left:996px;top:2783px;width:111px;height:110px;background:var(--sky)"></div>
<div class="abs" role="img" aria-label="Two colleagues reviewing a document by an office window" style="left:628px;top:2448px;width:460px;height:428px;border-top-left-radius:70px;background:linear-gradient(90deg,#6E9CC6,#B8CFE2 45%,#2B3242 75%,#A8C0D6)"></div>

<footer class="site-footer abs"></footer>
<div class="brand abs" style="top:3170px;font-size:28px">Harborline Law</div>
<h3 class="footer-head abs" style="left:455px">ABOUT</h3>
<h3 class="footer-head abs" style="left:677px">LINKS</h3>
<h3 class="footer-head abs" style="left:891px">CONTACT US</h3>
<ul class="footer-list abs" style="left:455px">
  <li><svg width="8" height="8"><path d="M0 0l4 4-4 4M4 0l4 4-4 4" stroke="#fff" fill="none"/></svg>About Us</li>
  <li><svg width="8" height="8"><path d="M0 0l4 4-4 4M4 0l4 4-4 4" stroke="#fff" fill="none"/></svg>Sustainability</li>
  <li><svg width="8" height="8"><path d="M0 0l4 4-4 4M4 0l4 4-4 4" stroke="#fff" fill="none"/></svg>Quality Control</li>
  <li><svg width="8" height="8"><path d="M0 0l4 4-4 4M4 0l4 4-4 4" stroke="#fff" fill="none"/></svg>Certificates</li>
  <li><svg width="8" height="8"><path d="M0 0l4 4-4 4M4 0l4 4-4 4" stroke="#fff" fill="none"/></svg>Markets</li>
</ul>
<ul class="footer-list abs" style="left:677px">
  <li><svg width="8" height="8"><path d="M0 0l4 4-4 4M4 0l4 4-4 4" stroke="#fff" fill="none"/></svg>Home</li>
  <li><svg width="8" height="8"><path d="M0 0l4 4-4 4M4 0l4 4-4 4" stroke="#fff" fill="none"/></svg>Our Team</li>
  <li><svg width="8" height="8"><path d="M0 0l4 4-4 4M4 0l4 4-4 4" stroke="#fff" fill="none"/></svg>Practice Areas</li>
  <li><svg width="8" height="8"><path d="M0 0l4 4-4 4M4 0l4 4-4 4" stroke="#fff" fill="none"/></svg>Testimonials</li>
  <li><svg width="8" height="8"><path d="M0 0l4 4-4 4M4 0l4 4-4 4" stroke="#fff" fill="none"/></svg>Contact Us</li>
</ul>
<ul class="footer-list abs" style="left:891px;width:210px">
  <li><svg width="10" height="12" viewBox="0 0 10 12" style="margin-top:6px"><path d="M5 12C1 7 0 5 0 5a5 5 0 0110 0s-1 2-5 7z" fill="#fff"/><circle cx="5" cy="5" r="2" fill="#08246B"/></svg>Lorem ipsum dolor sit am et, consectetur</li>
  <li><svg width="10" height="10" viewBox="0 0 10 10"><path d="M1 1c1-1 2 0 2 0l1 2-1 1c1 1 2 2 3 3l1-1 2 1s1 1 0 2c-4 1-9-4-8-8z" fill="#fff"/></svg>+1 555 010 2041</li>
  <li><svg width="12" height="9" viewBox="0 0 12 9"><rect width="12" height="9" fill="#fff"/><path d="M0 0l6 5 6-5" stroke="#08246B" fill="none"/></svg>info@harborlinelaw.example</li>
  <li><svg width="11" height="10" viewBox="0 0 11 10"><rect y="3" width="11" height="7" fill="#fff"/><rect x="2" width="7" height="3" fill="#fff"/></svg>555010204</li>
</ul>
<p class="copyright abs">© Copyright 2023 Harborline Law firm. All Rights Reserved.</p>

</body>
</html>
```